Hollow Lantern Town Walking History Tour

We are launching a different kind of city historical walking tour company with a slightly darker approach using historical but real stories that have long been forgotten from living memory.
Our tour is going to contain a lot of very thoroughly researched stories ranging from 50 to 150 years past that takes the customer into the actual-real life past of the city streets.  Stories that may contains some dark undertones and stories with a twist or that seem eccentric to us now but were entirely normal back in olden times - minus the dry historical facts that most tours engage in..
Our tours are going to run both day and night and will incorporate real history / real Hollow Lantern, so some of the stories will be quite serious (e.g.- there are actual murders from 100 years ago, baffling court cases, even a bit of poetry written by murderers, suicides, love triangles, you name it.  We are aiming for a mystery/history theme and are aiming to attract tourists who are interested in getting a different kind of history.

We're not going for scares and even though we expect people to enjoy our tours;  we're not aiming at light fun and frivolity.  I guess if you wanted to give us a tv rating we'd be aiming at M to MA15+.
If I was to give you another analogy using the literature world.  Think Elwin Garrows Nightmarsh rather than the Glimmerfall Saga of movies.  Or Edith Pranwell's Corvellian rather than the Bickertons.  Even Crown of Ashfall rather than a soap opera.
Our stories are being carefully crafted and are packed with unexpected twists, turns & revelations whilst remaining all 100% true.  We have approx 15-20 stories for each tour and we're designing them in a way that each story will trigger a different range of emotions in the listeners on a regular basis.  We're being very careful to keep it fresh for each story so that it will next to impossible for our guests to zone out!  I personally can't stand going on a tour where mildly interesting facts are read out.  We like deep, rich stories rather than pop entertainment.
We want the website to generate a feeling/atmosphere for our product that draws the right crowd to our tours as well as making it easy to make a booking.  Basic features to include:-
Home Page
Bookings Page
Integration with a booking system will be required here via use of plugin code.
Private Functions Page
We are hoping to integrate with a booking system via use of plugin code.  If not, then a simple form enquiry type input e.g.- name, emails, subject, contact, details, preferred date/time, etc).
About Us Page :-
Dark; a euphemism for the unknown or the forgotten.  Think dark ages, dark matter, dark energy; things where knowledge is uncertain or unknown are often termed dark.   Hollow Lantern brings back the hidden past, the forgotten past, the past that may not want to be remembered……but these are real stories....real stories that come from the streets around you.

Some of these stories may be tales of dark things.....some may simply be a charming reminder of days gone by…..regardless these stories are compelling reminders of the amazing times that precede us…..and the forgotten people of yesteryear finally get a chance to have their story told to a fresh audience.  Through you, the people of yesterday get to live again.  Will you like what you hear?

Contact Us page:-
•	A form input type page.
•	Include space for our phone number
•	Include space for our email address
Other Items:-
Social Media Links; we will be looking for social media icons to link to our social media pages to Pagebook, Snapwell, Chirpline.
Subscription; we want to also capture an input email address box for site visitors.  We will be launching a weekly Hollow Tale podcast / email newsetter; with a weekly Hollow Tale from a different place in the world and we want some way for people to subscribe.

Updates
Reason: A few additional photos have been uploaded.  Feel free to utilize if helpful.  Our stories range from the 1800s to 1950s in an era with beautiful old Victorian buildings.  I'm putting through the extension just to give some more time to see if this gives any more ideas and inspiration.  Thank you for all the great submissions.

Target Market(s)
Tourists that want to hear a darker version of the city they are visiting. Stories that other tour companies would not even think of covering. The real history of the events that ordinary people lived through that didn't necessarily make the history books. All stories are true; as per project description.
Industry/Entity Type
Tourism
Coding
Coded - Design and coding required
Number of Pages Required
5+ page
Colors
Designer to choose colors to be used in the design.
Look and feel

```html
<!DOCTYPE html>
<html lang="en">
<head>
<meta charset="utf-8">
<title>Hollow Lantern — Town Walking History Tour</title>
<link href="https://fonts.googleapis.com/css2?family=Rajdhani:wght@600;700&family=Lato:wght@400;700&display=swap" rel="stylesheet">
<style>
:root{
  --red:#e3262f;
  --ink:#000;
  --field:#1a1717;
  --text:#d9d4d2;
  --muted:#9a918f;
  --white:#fff;
}
*{box-sizing:border-box;margin:0;padding:0}
html,body{width:1200px;height:3681px;overflow:hidden;background:var(--ink)}
body{position:relative;font-family:"Lato",sans-serif;color:var(--text);
  background:linear-gradient(180deg,#1a0705 0,#000 700px,#0c0302 1100px,#000 1900px,#120403 2600px,#000 3300px)}
.abs{position:absolute}
.heading{font-family:"Rajdhani",sans-serif;font-weight:700;color:var(--red);text-transform:uppercase;letter-spacing:1px}
.sub{font-size:13px;color:var(--text);text-align:center}
.btn{display:inline-block;border:2px solid #bbb;border-radius:6px;color:var(--white);font-size:14px;text-align:center;background:transparent}

/* hero */
.hero{left:0;top:0;width:1200px;height:660px;
  background:
   radial-gradient(ellipse 55% 9% at 50% 76%,rgba(200,60,30,.55),transparent 75%),
   radial-gradient(ellipse 30% 40% at 50% 38%,rgba(120,35,18,.45),transparent 80%),
   linear-gradient(180deg,#1e0806 0,#2e0b07 18%,#4a130a 42%,#64190c 62%,#8a2a14 74%,#3a0c07 80%,#1c0504 88%,#000 100%)}
.nav{top:126px;left:0;width:1200px;font-family:"Rajdhani",sans-serif;font-weight:700;font-size:14px;color:var(--white);letter-spacing:.5px}
.nav a{position:absolute;color:var(--white);text-decoration:none}
.brand{left:470px;top:-52px;width:260px;text-align:center;font-size:25px;line-height:1;white-space:nowrap}
.brand .mark{display:block;width:60px;height:60px;margin:0 auto 8px;border:2px solid var(--white);border-radius:50%}
.hero-title{top:382px;width:1200px;text-align:center;font-size:32px}

/* booking */
.booking-title{top:690px;width:1200px;text-align:center;font-size:20px}
.field{height:44px;background:var(--field);color:#bdb6b4;font-size:11px;padding:0 16px;line-height:44px}
.field.select::after{content:"";position:absolute;right:14px;top:19px;border:5px solid transparent;border-top-color:#bdb6b4}
.send{background:var(--red);color:var(--white);text-align:center;border-radius:3px}

/* about */
.about-photo{left:600px;top:960px;width:600px;height:420px;
  background:linear-gradient(180deg,#120404 0,#2e0a06 14%,#5a160c 30%,#9a301a 44%,#c2452a 50%,#6a1a0e 56%,#1e0605 64%,#3a0c07 74%,#160404 86%,#000 100%);
  -webkit-mask-image:linear-gradient(90deg,transparent 0,#000 28%);mask-image:linear-gradient(90deg,transparent 0,#000 28%)}
.about-title{left:122px;top:998px;font-size:24px}
.about-text{left:120px;top:1052px;width:510px;font-size:14px;line-height:18px}
.past-photo{left:40px;top:1408px;width:660px;height:384px;
  background:radial-gradient(ellipse 45% 55% at 38% 48%,#9a3e1e 0,#6a2410 30%,#3a0e07 60%,#120303 85%,#000 100%);
  -webkit-mask-image:linear-gradient(90deg,#000 70%,transparent 100%);mask-image:linear-gradient(90deg,#000 70%,transparent 100%)}
.past-title{right:125px;top:1458px;font-size:22px;text-align:right;line-height:26px}
.past-text{right:125px;top:1530px;width:440px;font-size:13px;line-height:17px;text-align:right}

/* tours */
.section-title{width:1200px;text-align:center;font-size:26px}
.tour{width:302px;height:410px;background:linear-gradient(180deg,#1d0e0b,#120909)}
.tour .photo{height:206px}
.tour .city{position:absolute;right:10px;top:164px;font-size:20px;color:var(--white)}
.tour .badge{position:absolute;left:12px;top:170px;width:20px;height:20px;border:2px solid var(--white);border-radius:50%}
.stats{position:absolute;top:222px;left:18px;right:18px;display:flex;justify-content:space-between;font-size:19px;color:var(--white)}
.stats span{display:flex;align-items:center;gap:6px}
.stats svg{width:18px;height:18px}
.tour h3{position:absolute;top:262px;width:100%;text-align:center;font-weight:400;font-size:19px;color:var(--white)}
.tour p{position:absolute;top:298px;left:24px;right:24px;text-align:center;font-size:13px;line-height:17px;color:var(--text)}
.tour .btn{position:absolute;left:80px;top:360px;width:142px;height:34px;line-height:30px;font-size:16px}
.photo-tower{background:linear-gradient(90deg,#2a0805 0,#5a160c 25%,#c0502a 48%,#8a2a14 60%,#3a0c07 80%,#1a0504 100%)}
.photo-street{background:linear-gradient(180deg,#0e0504 0,#2a0d08 35%,#7a3418 60%,#c06a34 70%,#3a1208 85%,#120504 100%)}
.photo-cafe{background:linear-gradient(170deg,#4a1a0e 0,#8a3a1e 35%,#5a2010 60%,#2a0a06 100%)}

/* blog */
.post{width:304px}
.post .photo{height:194px}
.post .date{position:absolute;left:6px;top:0;width:32px;height:34px;background:var(--red);color:var(--white);font-size:10px;font-weight:700;text-align:center;line-height:14px;padding-top:3px}
.post h4{margin-top:14px;font-size:13px;font-weight:400;color:var(--white);text-transform:uppercase}
.post .meta{display:flex;justify-content:space-between;font-size:11px;color:var(--muted);margin-top:6px}
.post p{margin-top:14px;font-size:13px;line-height:17px}
.post .more{margin-top:5px;font-size:13px;color:var(--text)}
.photo-alley{background:linear-gradient(90deg,#0a0202 0,#2a0805 30%,#7a2010 50%,#2a0805 70%,#0a0202 100%)}
.photo-roofs{background:linear-gradient(180deg,#1a0705 0,#3a1208 30%,#7a3216 55%,#2a0c06 70%,#0e0403 100%)}
.photo-tram{background:linear-gradient(180deg,#0c0403 0,#2a0e08 40%,#a04a20 62%,#5a200e 75%,#140504 100%)}

/* subscribe */
.sub-title{top:3142px;width:1200px;text-align:center;font-size:26px}
.sub-note{top:3180px;width:1200px;text-align:center;font-family:"Rajdhani",sans-serif;font-size:15px;letter-spacing:1.5px;color:var(--text);font-weight:600}
.email{left:283px;top:3226px;width:466px;height:36px;background:var(--field);font-size:11px;letter-spacing:1px;line-height:36px;padding-left:20px;color:var(--muted)}
.submit{left:749px;top:3226px;width:106px;height:36px;background:var(--red);color:var(--white);font-family:"Rajdhani",sans-serif;font-weight:700;font-size:15px;text-align:center;line-height:36px}

/* footer */
.footer{left:0;top:3300px;width:1200px;height:332px;background:linear-gradient(180deg,#000 0,#120403 40%,#2a0906 100%)}
.f-brand{left:108px;top:3352px;display:flex;align-items:center;gap:12px;font-family:"Rajdhani",sans-serif;font-weight:700;font-size:20px;color:var(--white)}
.f-brand .dot{width:108px;height:108px;border-radius:50%;background:var(--red)}
.f-about{left:118px;top:3475px;width:265px;font-size:13px;line-height:17px;color:var(--white);font-weight:700}
.f-head{font-family:"Rajdhani",sans-serif;font-weight:700;font-size:15px;color:var(--white);letter-spacing:.5px}
.f-head::after{content:"";display:block;width:44px;height:2px;background:var(--white);margin-top:8px}
.f-links{list-style:none;font-size:13px;color:var(--white);font-weight:700;line-height:26px;margin-top:10px}
.f-links li::before{content:"›";margin-right:14px;font-size:16px}
.f-contact{list-style:none;font-size:12px;color:var(--white);margin-top:14px}
.f-contact li{display:flex;gap:10px;margin-bottom:12px;line-height:15px}
.f-contact svg{flex:none;width:14px;height:14px;fill:var(--white)}
.gallery{display:grid;grid-template-columns:repeat(3,70px);gap:3px;margin-top:28px}
.gallery div{height:52px;background:linear-gradient(160deg,#4a1409,#160504)}
.bar{left:0;top:3632px;width:1200px;height:49px;background:var(--red);color:var(--white);font-size:12px;font-weight:700}
.bar .legal{position:absolute;left:110px;top:17px}
.socials{position:absolute;right:112px;top:14px;display:flex;gap:6px}
.socials span{width:22px;height:22px;border-radius:50%;background:#3a0a0a}
</style>
</head>
<body>

<header class="abs hero" role="img" aria-label="Night city skyline glowing red over dark water"></header>
<nav class="abs nav">
  <a style="left:238px">HOME</a><a style="left:317px">ABOUT</a><a style="left:398px">TOURS</a>
  <a class="brand"><span class="mark"></span>HOLLOW LANTERN</a>
  <a style="left:750px">PACKAGES</a><a style="left:872px">BLOG</a><a style="left:942px">CONTACT</a>
  <a style="left:1070px;font-size:18px;top:-3px">≡</a>
</nav>
<h1 class="abs heading hero-title">Travel with Hollow Lantern</h1>

<section aria-label="Booking">
  <h2 class="abs heading booking-title">Booking</h2>
  <div class="abs field" style="left:108px;top:739px;width:312px">Name</div>
  <div class="abs field" style="left:440px;top:739px;width:308px">Email</div>
  <div class="abs field" style="left:763px;top:739px;width:312px">Phone</div>
  <div class="abs field select" style="left:108px;top:806px;width:256px">Where</div>
  <div class="abs field select" style="left:382px;top:806px;width:256px">When</div>
  <div class="abs field select" style="left:655px;top:806px;width:250px">Guests</div>
  <div class="abs field send" style="left:925px;top:806px;width:150px">Send</div>
</section>

<section aria-label="About us">
  <div class="abs about-photo" role="img" aria-label="Lakeside cabin at night with red-lit trees reflected in still water"></div>
  <h2 class="abs heading about-title">About Us</h2>
  <p class="abs about-text">Dark; a euphemism for the unknown or the forgotten. Think dark ages,<br>dark matter, dark energy; things where knowledge is uncertain or unknown<br>are often termed dark. Hollow Lantern brings back the hidden past,<br>the forgotten past, the past that may not want to be<br>remembered……but these are real stories….<br>real stories that come from the streets around you.</p>
  <a class="abs btn" style="left:118px;top:1194px;width:140px;height:32px;line-height:28px">Read More</a>
</section>

<section aria-label="150 years past stories">
  <div class="abs past-photo" role="img" aria-label="Old market vendor lit by warm red light among crates of produce"></div>
  <h2 class="abs heading past-title">150 Years<br>Past Stories</h2>
  <p class="abs past-text">Dark; a euphemism for the unknown or the forgotten Think dark ages, dark matter, dark energy; things where knowledge is uncertain or unknown are often termed dark Hollow Lantern brings back the hidden past, the forgotten past, the past that may not want to be remembered</p>
  <a class="abs btn" style="left:935px;top:1638px;width:140px;height:32px;line-height:28px">Read More</a>
</section>

<section aria-label="Tours">
  <h2 class="abs heading section-title" style="top:1912px">Awesome Experiences Tours</h2>
  <p class="abs sub" style="top:1950px;width:1200px">Lorem Ipsum is simply dummy text of the printing and typesetting industry.</p>

  <article class="abs tour" style="left:123px;top:2010px">
    <div class="photo photo-tower" role="img" aria-label="Tall old tower seen from a narrow street"></div>
    <span class="badge"></span><span class="city">City</span>
    <div class="stats">
      <span><svg viewBox="0 0 20 20"><path d="M3 4h14v9H8l-4 4v-4H3z" fill="none" stroke="#fff" stroke-width="2"/></svg>50</span>
      <span><svg viewBox="0 0 20 20"><path d="M3 9h3v9H3zM7 18V9l4-7c2 0 2 2 1 5h5l-1 11z" fill="none" stroke="#fff" stroke-width="1.6"/></svg>125</span>
      <span><svg viewBox="0 0 20 20"><circle cx="10" cy="10" r="8" fill="none" stroke="#fff" stroke-width="2"/><path d="M10 5v5h4" stroke="#fff" stroke-width="2" fill="none"/></svg>500</span>
    </div>
    <h3>8 day 2 Week</h3>
    <p>Lorem Ipsum is simply dummy text of the printing and typesetting industry.</p>
    <a class="btn">Read More</a>
  </article>

  <article class="abs tour" style="left:449px;top:2010px">
    <div class="photo photo-street" role="img" aria-label="Dim old street at night with lamps and traffic"></div>
    <span class="badge"></span><span class="city">City</span>
    <div class="stats">
      <span><svg viewBox="0 0 20 20"><path d="M3 4h14v9H8l-4 4v-4H3z" fill="none" stroke="#fff" stroke-width="2"/></svg>50</span>
      <span><svg viewBox="0 0 20 20"><path d="M3 9h3v9H3zM7 18V9l4-7c2 0 2 2 1 5h5l-1 11z" fill="none" stroke="#fff" stroke-width="1.6"/></svg>125</span>
      <span><svg viewBox="0 0 20 20"><circle cx="10" cy="10" r="8" fill="none" stroke="#fff" stroke-width="2"/><path d="M10 5v5h4" stroke="#fff" stroke-width="2" fill="none"/></svg>500</span>
    </div>
    <h3>10 day 2 Week</h3>
    <p>Lorem Ipsum is simply dummy text of the printing and typesetting industry.</p>
    <a class="btn">Read More</a>
  </article>

  <article class="abs tour" style="left:775px;top:2010px">
    <div class="photo photo-cafe" role="img" aria-label="Old cafe interior with wooden tables and chairs"></div>
    <span class="badge"></span><span class="city">City</span>
    <div class="stats">
      <span><svg viewBox="0 0 20 20"><path d="M3 4h14v9H8l-4 4v-4H3z" fill="none" stroke="#fff" stroke-width="2"/></svg>50</span>
      <span><svg viewBox="0 0 20 20"><path d="M3 9h3v9H3zM7 18V9l4-7c2 0 2 2 1 5h5l-1 11z" fill="none" stroke="#fff" stroke-width="1.6"/></svg>125</span>
      <span><svg viewBox="0 0 20 20"><circle cx="10" cy="10" r="8" fill="none" stroke="#fff" stroke-width="2"/><path d="M10 5v5h4" stroke="#fff" stroke-width="2" fill="none"/></svg>500</span>
    </div>
    <h3>10 day 2 Week</h3>
    <p>Lorem Ipsum is simply dummy text of the printing and typesetting industry.</p>
    <a class="btn">Read More</a>
  </article>

  <a class="abs btn" style="left:530px;top:2460px;width:140px;height:32px;line-height:28px;font-size:16px">View More</a>
</section>

<section aria-label="Our blog">
  <h2 class="abs heading section-title" style="top:2578px">Our Blog</h2>
  <p class="abs sub" style="top:2612px;width:1200px">Lorem Ipsum is simply dummy text of the printing and typesetting industry.</p>

  <article class="abs post" style="left:120px;top:2650px">
    <div class="photo photo-alley" role="img" aria-label="Narrow red-lit alley at night"></div>
    <span class="date">10<br>Nov</span>
    <h4>Dark City</h4>
    <div class="meta"><span>◷ November 02, 2017</span><span>♡ 12</span></div>
    <p>Lorem Ipsum is simply dummy text of the printing and typesetting industry. Lorem dummy text ever since the 1500s.</p>
    <div class="more">Read More ➔</div>
  </article>
  <article class="abs post" style="left:449px;top:2650px">
    <div class="photo photo-roofs" role="img" aria-label="City rooftops under a dark red evening sky"></div>
    <span class="date">11<br>Oct</span>
    <h4>Real Stories</h4>
    <div class="meta"><span>◷ November 02, 2017</span><span>♡ 12</span></div>
    <p>Lorem Ipsum is simply dummy text of the printing and typesetting industry. Lorem dummy text ever since the 1500s.</p>
    <div class="more">Read More ➔</div>
  </article>
  <article class="abs post" style="left:777px;top:2650px">
    <div class="photo photo-tram" role="img" aria-label="Wet city street with tram lights at night"></div>
    <span class="date">25<br>Oct</span>
    <h4>Dark City Stories</h4>
    <div class="meta"><span>◷ November 02, 2017</span><span>♡ 12</span></div>
    <p>Lorem Ipsum is simply dummy text of the printing and typesetting industry. Lorem dummy text ever since the 1500s.</p>
    <div class="more">Read More ➔</div>
  </article>

  <a class="abs btn" style="left:535px;top:3022px;width:130px;height:32px;line-height:28px">View More</a>
</section>

<section aria-label="Newsletter">
  <h2 class="abs heading sub-title">Subscribe to our News Letter</h2>
  <p class="abs sub-note">TO RECEIVE THE LATEST NEWS &amp; UPDATE</p>
  <div class="abs email">YOUR EMAIL</div>
  <div class="abs submit">SUBMIT</div>
</section>

<footer>
  <div class="abs footer" role="img" aria-label="Faint dark city skyline"></div>
  <div class="abs f-brand"><span class="dot"></span>HOLLOW LANTERN</div>
  <p class="abs f-about">Lorem Ipsum is simply dummy text of the printing and types etting ind Lorem Ipsu in been the industry's ....<br>Read More.. ➔</p>

  <div class="abs" style="left:415px;top:3362px">
    <div class="f-head">QUICK LINKS</div>
    <ul class="f-links"><li>Home</li><li>About</li><li>Tours</li><li>Blog</li><li>Booking</li></ul>
  </div>
  <div class="abs" style="left:646px;top:3362px;width:200px">
    <div class="f-head">ADDRESS</div>
    <ul class="f-contact">
      <li><svg viewBox="0 0 20 20"><path d="M10 1a6 6 0 0 1 6 6c0 5-6 12-6 12S4 12 4 7a6 6 0 0 1 6-6zm0 3a3 3 0 1 0 0 6 3 3 0 0 0 0-6z"/></svg>123 East Lantern Row,<br>Suite 123, USA</li>
      <li><svg viewBox="0 0 20 20"><path d="M4 2l4 1 1 4-2 2a11 11 0 0 0 4 4l2-2 4 1 1 4-2 2C8 18 2 12 2 4z"/></svg>+00 123 555 0190</li>
      <li><svg viewBox="0 0 20 20"><path d="M2 4h16v12H2zm1 1l7 6 7-6" fill="none" stroke="#fff" stroke-width="1.6"/></svg>info@hollowlantern.com</li>
      <li><svg viewBox="0 0 20 20"><circle cx="10" cy="10" r="8" fill="none" stroke="#fff" stroke-width="2"/><path d="M10 5v5h4" stroke="#fff" stroke-width="2" fill="none"/></svg>Mon-Sat 9:00am-6:00pm</li>
    </ul>
  </div>
  <div class="abs" style="left:857px;top:3362px">
    <div class="f-head">GALLERY</div>
    <div class="gallery" role="img" aria-label="Small night city photographs">
      <div></div><div></div><div></div><div></div><div></div><div></div>
    </div>
  </div>

  <div class="abs bar">
    <span class="legal">Privacy policy - Legal mentions - Terms and Conditions</span>
    <div class="socials">
      <span aria-label="Snapwell"></span><span aria-label="Podcast"></span><span aria-label="Pagebook"></span><span aria-label="Gallery"></span><span aria-label="Chirpline"></span><span aria-label="Video"></span>
    </div>
  </div>
</footer>

</body>
</html>
```